Redesign a TV Station website

Hello,
it looks like my explaination was not clear enough so i would like to clarify.
We are no longer designing a news website but rather a website for our TV station.
Please take a look at the current website we have .
http://www.vko.ci
We want a website similar to these two websites as example.

Please use the following websites as example
https://www.lumatel.com/
https://www.drw.com/

Here are my main menu on the horizontal bar
Accueil | Films | Series | Enfants | TV en Direct
P/S: You should disregard previous designs for the news website. We are designing purely a website for the TV stations. Please take a look at current site we have and design it similar to these two examples i mentioned
https://www.lumatel.com/
https://www.drw.com/
Updates

I needed more info for the project update.

Hello, We have updated design requirement for our project and hope it is much easier for you. You need to design the page based on the content on the link below: http://587opratv.com/template_obs.pdf You should use the same design as this to design the page http://587opratv.com/marc.jpeg The page will have same header style, color and design as the last link. However the content and layout of the page is the same as the first link. Please disregard the section that says "PAGE TYPE POUR MOBILE VERSION" Also disregard the title "MINI SITE LES ARPENTEURS "

Target Market(s)

TV Station

Number of Pages Required

1 page

Font styles to use
Sans Serif

Colors

Designer to choose colors to be used in the design.

Requirements
Must have
• N/A
Nice to have
• N/A
Should not have
• N/A

```html
<!DOCTYPE html>
<html lang="fr">
<head>
<meta charset="utf-8">
<title>KVA.info — TV</title>
<link rel="stylesheet" href="https://fonts.googleapis.com/css2?family=Roboto:wght@400;500;700&family=Roboto+Condensed:wght@400;700&display=swap">
<style>
:root{
  --orange:#f7a21b;
  --blue:#10a5e8;
  --dark:#2b2829;
  --ink:#222;
  --muted:#9a9a9a;
  --line:#e6e6e6;
  --grey-band:#f1f1f1;
  --white:#fff;
}
*{box-sizing:border-box;margin:0;padding:0}
html,body{width:1200px;height:4758px;overflow:hidden}
body{font-family:"Roboto",sans-serif;color:var(--ink);background:var(--white);position:relative}
.wrap{position:absolute;left:98px;width:1004px}
.img{display:block;background:linear-gradient(135deg,#7d6a5c,#2f3a4a)}
.img.warm{background:linear-gradient(135deg,#c9a27b,#5b3b2a)}
.img.sky{background:linear-gradient(180deg,#9fc1dc,#d9dfe4 70%,#8a8f94)}
.img.car{background:linear-gradient(135deg,#1b3fa8,#5f8fe0 50%,#1a1a1a)}
.img.city{background:linear-gradient(160deg,#f4d28a,#b77a3a 60%,#6b5544)}
.img.studio{background:linear-gradient(135deg,#8b8a86,#3e3a36)}
.img.red{background:linear-gradient(135deg,#e2452c,#8a1a10)}
.img.night{background:linear-gradient(135deg,#3b4a6b,#111a2a)}
.meta{font-size:9px;letter-spacing:.06em;text-transform:uppercase;color:var(--muted)}
.meta b{font-weight:500}
.meta.light{color:#fff}
.cond{font-family:"Roboto Condensed",sans-serif}
.btn-outline{display:inline-block;border:1px solid #fff;color:#fff;font-size:11px;padding:6px 16px}

/* header */
.topbar{position:absolute;top:0;left:0;width:1200px;height:52px}
.socials{position:absolute;left:98px;top:22px;display:flex;gap:8px}
.socials i{display:block;width:13px;height:13px;border-radius:50%;background:var(--blue)}
.socials i:nth-child(3){background:#e2457a}.socials i:nth-child(4){background:#3bb34a}
.logo{position:absolute;left:0;width:1200px;top:14px;text-align:center;font-size:25px;font-weight:700;color:var(--ink)}
.pills{position:absolute;right:98px;top:18px;display:flex;gap:12px}
.pill{font-size:10px;color:#fff;border-radius:12px;padding:5px 0;width:74px;text-align:center;background:var(--blue)}
.pill.orange{background:var(--orange)}
.nav{position:absolute;top:52px;left:0;width:1200px;height:36px;border-top:1px solid var(--line);border-bottom:1px solid var(--line)}
.nav ul{list-style:none;display:flex;justify-content:center;gap:38px;font-size:11px;line-height:36px}
.burger{position:absolute;left:98px;top:13px;width:14px;height:10px;border-top:2px solid var(--ink);border-bottom:2px solid var(--ink)}
.burger:after{content:"";position:absolute;left:0;right:0;top:2px;border-top:2px solid var(--ink)}
.search{position:absolute;right:98px;top:11px}

/* hero */
.hero{position:absolute;top:88px;left:0;width:1200px;height:475px;overflow:hidden;background:linear-gradient(90deg,#3a2a24 0%,#7a5a48 35%,#2e2b33 60%,#1d2030 100%)}
.hero-text{position:absolute;left:98px;top:75px;width:410px;color:#fff}
.hero-text h1{font-family:"Roboto Condensed",sans-serif;font-size:34px;line-height:42px;font-weight:700;margin:12px 0 60px}
.recent{position:absolute;left:606px;top:186px;color:#fff;font-weight:700;font-size:17px}
.recent-row{position:absolute;left:608px;top:234px;display:flex;gap:15px}
.rcard{width:240px;background:#fff;flex:none}
.rcard .img{height:135px}
.rcard .body{padding:12px 22px 20px;height:88px}
.rcard p{font-size:11px;line-height:15px;font-weight:500;margin-top:8px}

/* section titles */
.stitle{position:relative;height:36px;border-bottom:1px solid var(--line);display:flex;align-items:flex-end;justify-content:space-between}
.stitle h2{font-size:13px;font-weight:700;color:var(--dark);background:var(--orange);padding:0 64px 0 14px;height:36px;line-height:36px;clip-path:polygon(0 0,78% 0,100% 100%,0 100%)}
.tabs{display:flex;gap:22px;align-items:center;font-size:10px;margin-bottom:10px}
.tabs .on{background:var(--orange);color:#fff;border-radius:10px;padding:2px 11px}
.dark .stitle{border-color:#444}.dark .tabs{color:#ddd}
.arrows{font-size:14px;color:var(--muted);margin-bottom:8px;letter-spacing:12px}

/* featured */
.featured{top:608px}
.feat-grid{position:absolute;top:52px;display:grid;grid-template-columns:240px 496px 240px;gap:14px}
.small-item{margin-bottom:20px}
.small-item .img{height:135px;margin-bottom:12px}
.small-item p{font-size:12px;line-height:16px;font-weight:500;margin-top:6px}
.big-tile{position:relative;height:322px;margin-bottom:16px;color:#fff}
.big-tile .caption{position:absolute;left:22px;bottom:24px;right:30px}
.big-tile h3{font-family:"Roboto Condensed",sans-serif;font-size:22px;line-height:26px;font-weight:700;margin:6px 0 18px}
.ad-black{background:#000}
.list-row{display:flex;gap:14px;height:75px;align-items:flex-start}
.list-row .img{width:60px;height:60px;flex:none}
.list-row p{font-size:11px;line-height:15px;font-weight:500;margin-top:4px}
.list-row .meta{margin-top:2px}
.banner{position:absolute;top:756px;width:1004px;height:74px;display:flex;border:1px solid var(--line)}
.banner .brand{width:375px;display:flex;align-items:center;justify-content:center;gap:12px;font-size:24px;font-weight:500;color:var(--dark)}
.banner .brand i{width:14px;height:14px;border-radius:50%;background:var(--blue)}
.banner .cta{flex:1;background:var(--blue);color:#fff;font-size:13px;display:flex;align-items:center;justify-content:space-between;padding:0 24px 0 30px}
.banner .cta span{background:#fff;color:var(--blue);font-size:10px;font-weight:500;border-radius:14px;padding:7px 24px}

/* broadcast */
.band-dark{position:absolute;top:1484px;left:0;width:1200px;height:547px;background:var(--dark);color:#fff}
.broadcast{top:45px}
.bc-grid{position:absolute;top:52px;display:grid;grid-template-columns:495px 495px;gap:14px}
.video{position:relative;height:405px}
.play{position:absolute;width:44px;height:44px;border-radius:50%;background:#fff;display:flex;align-items:center;justify-content:center}
.play:after{content:"";border-left:13px solid var(--dark);border-top:8px solid transparent;border-bottom:8px solid transparent;margin-left:4px}
.video .play{left:226px;top:180px}
.vrow{display:flex;gap:15px;height:105px}
.vrow .img{position:relative;width:150px;height:90px;flex:none}
.vrow .play{width:30px;height:30px;left:14px;top:14px}
.vrow .play:after{border-left-width:9px;border-top-width:6px;border-bottom-width:6px}
.vrow p{font-size:12px;line-height:17px;font-weight:500;margin-top:6px;width:320px}
.vrow .meta{margin-top:10px;color:#bbb}

.ad-wide{position:absolute;top:2077px;left:98px;width:1004px;height:133px;background:#000}

/* card rows */
.cards4{position:absolute;top:52px;display:grid;grid-template-columns:repeat(4,240px);gap:14px}
.ccard{position:relative;height:210px;color:#fff}
.ccard .caption{position:absolute;left:22px;right:20px;bottom:28px}
.ccard p{font-size:13px;line-height:18px;font-weight:500;margin-top:6px}
.thinktank{top:2260px}

.band-grey{position:absolute;top:2566px;left:0;width:1200px;height:572px;background:var(--grey-band)}
.press{top:45px}
.pr-grid{position:absolute;top:52px;display:grid;grid-template-columns:495px 240px 240px;gap:14px}
.pr-big{position:relative;height:435px;color:#fff}
.pr-big .caption{position:absolute;left:22px;right:40px;bottom:24px}
.pr-item .img{height:135px;margin-bottom:12px}
.pr-item{margin-bottom:18px}
.pr-item p{font-size:12px;line-height:16px;font-weight:500;margin-top:6px}

.advertorial{top:3188px}

/* verifiers + radio */
.verifiers{top:3478px;width:750px}
.ver-grid{position:absolute;top:52px;display:grid;grid-template-columns:240px 240px 240px;gap:14px}
.side-ad{position:absolute;top:3494px;left:862px;width:240px;height:582px;background:#000}
.radio{top:3800px;width:750px}
.radio .stitle h2{padding-left:120px}
.radio-badge{position:absolute;left:14px;top:-14px;width:80px;height:80px;border-radius:50%;background:#fff;box-shadow:0 2px 8px rgba(0,0,0,.15);display:flex;align-items:center;justify-content:center}
.radio-badge i{width:40px;height:40px;border-radius:50%;background:var(--orange)}
.radio-grid{position:absolute;top:72px;display:grid;grid-template-columns:repeat(3,240px);gap:14px}
.radio-grid .img{height:135px;margin-bottom:20px}
.radio-grid p{font-size:12px;line-height:17px;font-weight:500}

/* survey */
.survey{position:absolute;top:4122px;left:98px;width:1004px;height:78px;background:var(--grey-band);display:flex;align-items:center}
.survey .tag{height:78px;width:222px;background:var(--orange);clip-path:polygon(0 0,100% 0,88% 100%,0 100%);display:flex;align-items:center;padding-left:30px;gap:10px;font-size:22px;font-weight:700;color:var(--dark)}
.survey .q{font-size:11px;line-height:16px;color:#555;width:460px;margin-left:20px}
.survey .btns{margin-left:auto;margin-right:24px;display:flex;gap:16px}
.survey .btns span{width:88px;text-align:center;border-radius:16px;padding:8px 0;font-size:11px;color:#fff;background:var(--blue)}
.survey .btns span+span{background:var(--orange)}

/* footer */
.footer{position:absolute;top:4242px;left:0;width:1200px;height:516px;background:var(--dark);color:#fff}
.fcol{position:absolute;top:48px}
.fcol h4{font-size:13px;font-weight:700;margin-bottom:8px}
.fcol ul{list-style:none;font-size:10.5px;line-height:22.5px;color:#aaa}
.fcol h4.gap{margin-top:22px}
.news p{font-size:10.5px;line-height:22px;color:#aaa;width:440px}
.email{margin-top:14px;width:336px;height:34px;border:1px solid #555;display:flex;justify-content:space-between;align-items:center;font-size:10px;color:#aaa;padding-left:14px}
.email span{background:var(--orange);color:#fff;height:100%;width:108px;display:flex;align-items:center;justify-content:center}
.fsoc{display:flex;gap:14px;margin-top:22px}
.fsoc i{width:18px;height:18px;background:#777;border-radius:3px}
.stores{display:flex;gap:16px;margin-top:28px}
.stores span{width:148px;height:42px;border:1px solid #777;border-radius:6px;display:flex;align-items:center;justify-content:center;font-size:15px;font-weight:500}
.legal{position:absolute;top:464px;left:98px;font-size:10px;color:#aaa;word-spacing:2px}
</style>
</head>
<body>

<header>
  <div class="topbar">
    <div class="socials"><i></i><i></i><i></i><i></i></div>
    <div class="logo">KVA.info</div>
    <div class="pills"><span class="pill">Video</span><span class="pill orange">Podcast</span></div>
  </div>
  <nav class="nav">
    <span class="burger"></span>
    <ul><li>Accueil</li><li>Films</li><li>Series</li><li>Enfants</li><li>TV en Direct</li></ul>
    <svg class="search" width="14" height="14" viewBox="0 0 14 14"><circle cx="6" cy="6" r="4.5" fill="none" stroke="#222" stroke-width="1.6"/><line x1="9.3" y1="9.3" x2="13" y2="13" stroke="#222" stroke-width="1.8"/></svg>
  </nav>
</header>

<section class="hero" role="img" aria-label="Photo of a politician speaking to a crowd of reporters with microphones">
  <div class="hero-text">
    <div class="meta light"><b>Society</b> · Mar 07</div>
    <h1>Lorem ipsum dolor sit amet, consectetur adipisc-ing elit, sed do eiusmod tempor</h1>
    <span class="btn-outline">Read Article</span>
  </div>
  <div class="recent">Recent News</div>
  <div class="recent-row">
    <article class="rcard"><div class="img warm" role="img" aria-label="Photo of a smiling woman"></div><div class="body"><div class="meta">Economies · Mar 07</div><p>It is a long established fact that a reader will be distracted ...</p></div></article>
    <article class="rcard"><div class="img night" role="img" aria-label="Photo of a speaker at a podium"></div><div class="body"><div class="meta">Politics · Mar 07</div><p>It is a long established fact that a reader will be distracted ...</p></div></article>
    <article class="rcard"><div class="img red" role="img" aria-label="Photo of a sports crowd"></div><div class="body"><div class="meta">Sport · Mar 07</div><p>It is a long established fact that a reader will be distracted ...</p></div></article>
  </div>
</section>

<section class="wrap featured">
  <div class="stitle"><h2>Featured News</h2><div class="tabs"><span class="on">All</span><span>Politics</span><span>Economies</span><span>Sport</span><span>Technologies</span><span>Society</span><span>Culture</span><span>Region</span></div></div>
  <div class="feat-grid">
    <div>
      <div class="small-item"><div class="img car" role="img" aria-label="Photo of a blue sports car"></div><div class="meta">Technologies · Mar 07</div><p>Sed ut perspiciatis unde omnis iste natus error sit voluptatem ...</p></div>
      <div class="small-item"><div class="img sky" role="img" aria-label="Photo of an airliner on the runway"></div><div class="meta">Society · Mar 07</div><p>Sed ut perspiciatis unde omnis iste natus error sit voluptatem ...</p></div>
      <div class="small-item"><div class="img city" role="img" aria-label="Photo of apartment buildings at sunset"></div><div class="meta">Culture · Mar 07</div><p>Sed ut perspiciatis unde omnis iste natus error sit voluptatem ...</p></div>
    </div>
    <div>
      <div class="big-tile img warm" role="img" aria-label="Portrait photo of a smiling woman"><div class="caption"><div class="meta light">Region · Mar 07</div><h3>At vero eos et accusamus et iusto odio dignissi-mos ducimus qui blanditiis praesentium.</h3><span class="btn-outline">Read Article</span></div></div>
      <div class="big-tile img" role="img" aria-label="Photo of a politician facing press microphones"><div class="caption"><div class="meta light">Politics · Mar 07</div><h3>At vero eos et accusamus et iusto odio dignissi-mos ducimus qui blanditiis praesentium.</h3><span class="btn-outline">Read Article</span></div></div>
    </div>
    <div>
      <div class="ad-black" style="height:210px;margin-bottom:20px"></div>
      <div class="list-row"><div class="img red" role="img" aria-label="Photo thumbnail"></div><div><div class="meta">Tech · Mar 07</div><p>At vero eos et accusamus et iusto odio dignissimos ...</p></div></div>
      <div class="list-row"><div class="img warm" role="img" aria-label="Photo thumbnail"></div><div><div class="meta">Economies · Mar 07</div><p>At vero eos et accusamus et iusto odio dignissimos ...</p></div></div>
      <div class="list-row"><div class="img night" role="img" aria-label="Photo thumbnail"></div><div><div class="meta">Sport · Mar 07</div><p>At vero eos et accusamus et iusto odio dignissimos ...</p></div></div>
      <div class="list-row"><div class="img studio" role="img" aria-label="Photo thumbnail"></div><div><div class="meta">Society · Mar 07</div><p>At vero eos et accusamus et iusto odio dignissimos ...</p></div></div>
      <div class="list-row"><div class="img" role="img" aria-label="Photo thumbnail"></div><div><div class="meta">Culture · Mar 07</div><p>At vero eos et accusamus et iusto odio dignissimos ...</p></div></div>
      <div class="list-row"><div class="img red" role="img" aria-label="Photo thumbnail"></div><div><div class="meta">Region · Mar 07</div><p>At vero eos et accusamus et iusto odio dignissimos ...</p></div></div>
    </div>
  </div>
  <div class="banner"><div class="brand"><i></i>Urban Media</div><div class="cta">Constructions your presence digital together<span>Learn More</span></div></div>
</section>

<section class="band-dark dark">
  <div class="wrap broadcast">
    <div class="stitle"><h2>Broadcast</h2><div class="tabs"><span class="on">All</span><span>News</span><span>Reports</span><span>Interview</span></div></div>
    <div class="bc-grid">
      <div class="video img studio" role="img" aria-label="Video still of a television studio with cameras">
        <span class="play"></span>
        <div style="position:absolute;left:22px;bottom:24px;right:40px"><div class="meta light">Interview · Mar 07</div><h3 class="cond" style="font-size:22px;line-height:26px;margin:6px 0 18px">At vero eos et accusamus et iusto odio dignissi-mos ducimus qui blanditiis praesentium.</h3><span class="btn-outline">Read Article</span></div>
      </div>
      <div>
        <div class="vrow"><div class="img warm" role="img" aria-label="Video thumbnail of a woman speaking"><span class="play"></span></div><div><div class="meta">News · Mar 07</div><p>Lorem ipsum dolor sit amet, consectetur adipiscing elit, sed do eiusmod tempor ...</p></div></div>
        <div class="vrow"><div class="img night" role="img" aria-label="Video thumbnail of a speaker at a podium"><span class="play"></span></div><div><div class="meta">Reports · Mar 07</div><p>Lorem ipsum dolor sit amet, consectetur adipiscing elit, sed do eiusmod tempor ...</p></div></div>
        <div class="vrow"><div class="img sky" role="img" aria-label="Video thumbnail of an airliner"><span class="play"></span></div><div><div class="meta">Interview · Mar 07</div><p>Lorem ipsum dolor sit amet, consectetur adipiscing elit, sed do eiusmod tempor ...</p></div></div>
        <div class="vrow"><div class="img city" role="img" aria-label="Video thumbnail of a woman in an office"><span class="play"></span></div><div><div class="meta">News · Mar 07</div><p>Lorem ipsum dolor sit amet, consectetur adipiscing elit, sed do eiusmod tempor ...</p></div></div>
      </div>
    </div>
  </div>
</section>

<div class="ad-wide"></div>

<section class="wrap thinktank">
  <div class="stitle"><h2>Think Tank</h2><div class="arrows">‹ ›</div></div>
  <div class="cards4">
    <div class="ccard img" role="img" aria-label="Portrait photo of a man"><div class="caption"><div class="meta light">Mar 07</div><p>At vero eos et accusamus et iusto odio dignissimos ducimus qui blanditiis ...</p></div></div>
    <div class="ccard img warm" role="img" aria-label="Photo of women laughing"><div class="caption"><div class="meta light">Mar 07</div><p>At vero eos et accusamus et iusto odio dignissimos ...</p></div></div>
    <div class="ccard img red" role="img" aria-label="Portrait photo of a woman"><div class="caption"><div class="meta light">Mar 07</div><p>At vero eos et accusamus et iusto odio dignissimos ducimus qui blanditiis ...</p></div></div>
    <div class="ccard img studio" role="img" aria-label="Portrait photo of an older woman"><div class="caption"><div class="meta light">Mar 07</div><p>At vero eos et accusamus et iusto odio dignissimos ...</p></div></div>
  </div>
</section>

<section class="band-grey">
  <div class="wrap press">
    <div class="stitle"><h2>Press Release</h2><div class="tabs"><span class="on">All</span><span>Newspaper</span><span>Magazine</span><span>International</span></div></div>
    <div class="pr-grid">
      <div class="pr-big img studio" role="img" aria-label="Photo of a television studio"><div class="caption"><div class="meta light">International · Mar 07</div><h3 class="cond" style="font-size:22px;line-height:26px;margin:6px 0 18px">At vero eos et accusamus et iusto odio dignissi-mos ducimus qui blanditiis praesentium.</h3><span class="btn-outline">Read Article</span></div></div>
      <div>
        <div class="pr-item"><div class="img" role="img" aria-label="Photo of a woman reading"></div><div class="meta">Newspaper · Mar 07</div><p>Sed ut perspiciatis unde omnis iste natus error sit voluptatem ...</p></div>
        <div class="pr-item"><div class="img warm" role="img" aria-label="Photo of a woman in an office"></div><div class="meta">Magazine · Mar 07</div><p>Sed ut perspiciatis unde omnis iste natus error sit voluptatem ...</p></div>
      </div>
      <div>
        <div class="list-row"><div class="img red" role="img" aria-label="Photo thumbnail"></div><div><div class="meta">Magazine · Mar 07</div><p>At vero eos et accusamus et iusto odio dignissimos ...</p></div></div>
        <div class="list-row"><div class="img warm" role="img" aria-label="Photo thumbnail"></div><div><div class="meta">International · Mar 07</div><p>At vero eos et accusamus et iusto odio dignissimos ...</p></div></div>
        <div class="list-row"><div class="img night" role="img" aria-label="Photo thumbnail"></div><div><div class="meta">Newspaper · Mar 07</div><p>At vero eos et accusamus et iusto odio dignissimos ...</p></div></div>
        <div class="list-row"><div class="img studio" role="img" aria-label="Photo thumbnail"></div><div><div class="meta">Magazine · Mar 07</div><p>At vero eos et accusamus et iusto odio dignissimos ...</p></div></div>
        <div class="list-row"><div class="img" role="img" aria-label="Photo thumbnail"></div><div><div class="meta">International · Mar 07</div><p>At vero eos et accusamus et iusto odio dignissimos ...</p></div></div>
        <div class="list-row"><div class="img red" role="img" aria-label="Photo thumbnail"></div><div><div class="meta">Newspaper · Mar 07</div><p>At vero eos et accusamus et iusto odio dignissimos ...</p></div></div>
      </div>
    </div>
  </div>
</section>

<section class="wrap advertorial">
  <div class="stitle"><h2>Advertorial</h2><div class="tabs"><span class="on">All</span><span>Society</span><span>Culture</span><span>Region</span></div></div>
  <div class="cards4">
    <div class="ccard img" role="img" aria-label="Portrait photo of a man"><div class="caption"><div class="meta light">Culture · Mar 07</div><p>At vero eos et accusamus et iusto odio dignissimos ducimus qui blanditiis ...</p></div></div>
    <div class="ccard img warm" role="img" aria-label="Photo of women laughing"><div class="caption"><div class="meta light">Society · Mar 07</div><p>At vero eos et accusamus et iusto odio dignissimos ...</p></div></div>
    <div class="ccard img red" role="img" aria-label="Portrait photo of a woman"><div class="caption"><div class="meta light">Region · Mar 07</div><p>At vero eos et accusamus et iusto odio dignissimos ducimus qui blanditiis ...</p></div></div>
    <div class="ccard img studio" role="img" aria-label="Portrait photo of an older woman"><div class="caption"><div class="meta light">Culture · Mar 07</div><p>At vero eos et accusamus et iusto odio dignissimos ...</p></div></div>
  </div>
</section>

<section class="wrap verifiers">
  <div class="stitle"><h2>Verifiers Info</h2><div class="tabs"><span class="on">All</span><span>Investigation</span><span>Records</span></div></div>
  <div class="ver-grid">
    <div class="small-item"><div class="img sky" role="img" aria-label="Photo of an airliner on the runway"></div><div class="meta">Investigation · Mar 07</div><p>Sed ut perspiciatis unde omnis iste natus error sit voluptatem ...</p></div>
    <div class="small-item"><div class="img city" role="img" aria-label="Photo of apartment buildings at sunset"></div><div class="meta">Records · Mar 07</div><p>Sed ut perspiciatis unde omnis iste natus error sit voluptatem ...</p></div>
    <div>
      <div class="list-row"><div class="img warm" role="img" aria-label="Photo thumbnail"></div><div><div class="meta">Investigation · Mar 07</div><p>At vero eos et accusamus et iusto odio dignissimos ...</p></div></div>
      <div class="list-row"><div class="img night" role="img" aria-label="Photo thumbnail"></div><div><div class="meta">Records · Mar 07</div><p>At vero eos et accusamus et iusto odio dignissimos ...</p></div></div>
      <div class="list-row"><div class="img studio" role="img" aria-label="Photo thumbnail"></div><div><div class="meta">Investigation · Mar 07</div><p>At vero eos et accusamus et iusto odio dignissimos ...</p></div></div>
    </div>
  </div>
</section>
<div class="side-ad"></div>

<section class="wrap radio">
  <div class="stitle"><h2>Radio Lagune</h2><div class="arrows">‹ ›</div></div>
  <div class="radio-badge"><i></i></div>
  <div class="radio-grid">
    <div><div class="img studio" role="img" aria-label="Photo of a studio microphone and mixing desk"></div><p>Quis nostrud exercitation ullamco laboris nisi ut aliquip ex ea</p></div>
    <div><div class="img warm" role="img" aria-label="Photo of a radio host with headphones"></div><p>Quis nostrud exercitation ullamco laboris nisi ut aliquip ex ea</p></div>
    <div><div class="img" role="img" aria-label="Photo of headphones on a mixing console"></div><p>Quis nostrud exercitation ullamco laboris nisi ut aliquip ex ea</p></div>
  </div>
</section>

<section class="survey">
  <div class="tag"><svg width="34" height="18" viewBox="0 0 34 18"><path d="M2 9l6 6L20 2M14 13l2 2L30 2" fill="none" stroke="#2b2829" stroke-width="2.4"/></svg>Survey</div>
  <p class="q"><b>Algeria:</b> do you think that the purging of general either the beginning of great cleaning against corruption?</p>
  <div class="btns"><span>Yes</span><span>No</span></div>
</section>

<footer class="footer">
  <div class="fcol" style="left:98px"><h4>Category</h4><ul><li>Newsflash</li><li>Dernieres News</li><li>Policy</li><li>Economy</li><li>Society</li><li>Culture</li><li>Region</li><li>Technology</li><li>Africa</li><li>International</li><li>Newspaper</li><li>Interviews</li><li>reports</li></ul></div>
  <div class="fcol" style="left:353px"><h4>Reply Topic</h4><ul><li>Reportages</li><li>Journaux</li><li>Magazine</li></ul><h4 class="gap">Participate</h4><ul><li>Contact KVA Info</li><li>Think Tank</li><li>The poll</li></ul><h4 class="gap">Lesson Verifier</h4><ul><li>The verifiers</li><li>The community</li><li>The articles</li><li>The Team</li><li>The Charter</li><li>Partners</li></ul></div>
  <div class="fcol news" style="left:608px"><h4>Subscribe to Our Newsletter</h4><p>Every Tuesday, receive the best of l African news and receive in preview the exclusivities of the point</p>
    <div class="email">Your e-mail address<span>Subscribe</span></div>
    <div class="fsoc"><i></i><i></i><i></i><i></i><i></i><i></i></div>
    <div class="stores"><span>App Market</span><span>Play Shop</span></div>
  </div>
  <div class="legal">Mentionslegales &nbsp;|&nbsp; Conditions Generales d'utilisation &nbsp;|&nbsp; Politique de protection des donnes &nbsp;|&nbsp; Cookies &nbsp;|&nbsp; CGU &nbsp;|&nbsp; Contacts</div>
</footer>

</body>
</html>
```